Hernia Mesh Lawsuit - Banner & Creatives

Looking for design of ad banners and email creative for my Hernia Mesh Lawsuit website. Call to action based email focused on conveying brand, messaging of "have you had surgery using a surgical mesh, possibly for a hernia or a C-section? You may be eligible to join a surgical mesh class action lawsuit " and "ACT NOW: Check Your Eligibility Now." Call to action of 'Get Your Free Evaluation' or 'Fast, Free, No Obligation Evaluation'. Can use any messaging and images from the current website https://www.vorlastaclaims.com/herniamesh/find-out-if-youre-eligible/ Please focus on imaging that matches the site. The final Ad Banners must be delivered in both JPG and PSD file formats. Ad Banners must follow OWC standards. The final Email creative must be done in repsonsive HTML as well as text for easy use and include Email Opt Out link etc. <br/>We need Ad Banners in the following sizes.<br/><br/>• 728x90 Leaderboard<br/>• 300x250 Inline Rectangle<br/>• 320x50 Mobile<br/>Target Market(s)<br/><br/>NATIONAL INJURY LAWSUIT - Have you or a loved one had surgery using a surgical mesh, possibly for a hernia or a C-section? You may be eligible to join a surgical mesh class action lawsuit if you had another surgery to remove the mesh or if you suffered any side effects, including: Bleeding Bowel obstruction Fluid buildup (seromas) Infection Mesh migration Nerve damage Pain To qualify, the surgical mesh can be of any type, including Vela-Pro, B-LOXTM, Marvelle’s NuvaflexTM or any other brand.<br/>Industry/Entity Type<br/><br/>Lawyer<br/>Coding<br/><br/>Coded - Design and coding required<br/>Number of Pages Required<br/><br/>1 page<br/>Font styles to use<br/>Sans Serif<br/>Look and feel<br/><br/>Each slider illustrates characteristics of the customer's brand and the style your logo design should communicate.<br/>Elegant<br/>Bold<br/>Playful<br/>Serious<br/>Traditional<br/>Modern<br/>Personable<br/>Professional<br/>Feminine<br/>Masculine<br/>Colorful<br/>Conservative<br/>Economical<br/>Upmarket<br/><br/>Requirements<br/>Must have<br/><br/>* Call to action ad banners and Email creative.<br/>* Ad Banners in the 3 sizes noted in the project description.<br/>* Email creative must also be coded in responsive HTML.<br/>* The design must match the website https://varnell-benefitforms.com/<br/><br/>Nice to have<br/><br/>* Strong call to action<br/><br/>Should not have<br/><br/>* Should not be cookie cutter. Stick to simple yet official looking.

Target Market(s)

People who had another surgery to remove the mesh or if you suffered any side effects, including:

Bleeding
Bowel obstruction
Fluid buildup (seromas)
Infection

Mesh migration
Nerve damage
Pain

To qualify, the surgical mesh can be of any type, including Vela-Pro, B-LOXTM, Marvelle’s NuvaflexTM or any other brand.

Industry/Entity Type

Legal

Font styles to use
Serif

Colors

Designer to choose colors to be used in the design.

Requirements
Must have
• Must have
• * Call to action ad banners and Email creative.
• * Ad Banners in the 3 sizes noted in the project description.
• * Email creative must also be coded in responsive HTML.
• * The design must match the website https://varnell-benefitforms.com/
Nice to have
• Nice to have
• * Strong call to action
Should not have
• Should not have
• * Should not be cookie cutter. Stick to simple yet official looking.

```html
<!DOCTYPE html>
<html lang="en">
<head>
<meta charset="utf-8">
<title>Hernia Mesh Lawsuit – Eligibility Banner</title>
<link rel="stylesheet" href="https://fonts.googleapis.com/css2?family=Montserrat:wght@600;700;800&family=Merriweather:wght@400&display=swap">
<style>
  :root {
    --deep-blue: #1b3a8c;
    --mid-blue: #2f5fb8;
    --violet: #5b3d9c;
    --magenta: #c23a86;
    --pink: #e0559a;
    --white: #ffffff;
    --sky: #4da9f2;
    --alert-red: #e3232c;
  }
  html, body {
    margin: 0;
    padding: 0;
    width: 1200px;
    height: 999px;
    overflow: hidden;
    background: var(--white);
  }
  .banner {
    position: relative;
    width: 1200px;
    height: 999px;
    overflow: hidden;
    color: var(--white);
  }
  .banner__photo {
    position: absolute;
    inset: 0;
    background:
      radial-gradient(ellipse 55% 60% at 88% 55%, rgba(224, 85, 154, 0.85), rgba(224, 85, 154, 0) 70%),
      radial-gradient(ellipse 45% 50% at 70% 25%, rgba(130, 80, 170, 0.6), rgba(130, 80, 170, 0) 70%),
      linear-gradient(100deg, var(--deep-blue) 0%, var(--mid-blue) 38%, var(--violet) 66%, var(--magenta) 100%);
  }
  .headline {
    position: absolute;
    left: 0;
    right: 0;
    margin: 0;
    text-align: center;
    font-family: "Montserrat", sans-serif;
    font-weight: 700;
    text-transform: uppercase;
    line-height: 1;
  }
  .headline__top {
    top: 56px;
    font-size: 84px;
    letter-spacing: 1px;
  }
  .headline__main {
    top: 150px;
    font-size: 128px;
    letter-spacing: 1px;
  }
  .message {
    position: absolute;
    left: 69px;
    top: 336px;
    width: 1100px;
    margin: 0;
    font-family: "Merriweather", serif;
    font-weight: 400;
    font-size: 37px;
    line-height: 57px;
  }
  .cta {
    position: absolute;
    left: 54px;
    top: 655px;
    margin: 0;
    font-family: "Montserrat", sans-serif;
    font-weight: 700;
    font-size: 126px;
    line-height: 1;
    color: var(--sky);
    letter-spacing: 1px;
  }
  .offer-band {
    position: absolute;
    left: 0;
    right: 0;
    bottom: 0;
    height: 147px;
    background: var(--alert-red);
    display: flex;
    align-items: center;
    justify-content: center;
    font-family: "Montserrat", sans-serif;
    font-weight: 600;
    font-size: 39px;
    letter-spacing: 2.5px;
    text-transform: uppercase;
  }
</style>
</head>
<body>
  <main class="banner">
    <div class="banner__photo" role="img" aria-label="Photo of a person in a grey sweater holding their side in pain, tinted with a blue to magenta colour wash"></div>
    <h1 class="headline headline__top">Injured from a hernia</h1>
    <p class="headline headline__main">Mesh surgery?</p>
    <p class="message">Have you had surgery using a surgical<br>mesh, possibly for a hernia or a C-section?<br>You may be eligible to join a surgical mesh<br>class action lawsuit</p>
    <p class="cta">ACT NOW</p>
    <div class="offer-band">Fast, free, no obligation evaluation</div>
  </main>
</body>
</html>
```